Business card design for new, innovative company - BluePlinth

We are a new company looking for a business card design that is fun, different and quirky. Must use corporate colour green - CMYK C:55, M:0, Y:100, K:0, and corporate colour grey - C:0, M:0, Y: 0, K:70.

We have developed the first real time data application, in which people are able to profile the data of their existing customers in order to pull out more good fit clients to direct their marketing activities at.

Industry/Entity Type

Marketing

Requirements
Must have
• Logo, name, title, telephone number, fax number, email, website, address

```html
<!DOCTYPE html>
<html lang="en">
<head>
<meta charset="utf-8">
<title>BluePlinth Business Card</title>
<link href="https://fonts.googleapis.com/css2?family=Open+Sans:wght@400;600;700&display=swap" rel="stylesheet">
<style>
  :root {
    --brand-green: #7cc11f;
    --brand-grey: #6d6e71;
    --card-paper: #e9e9e9;
    --backdrop: #8c8c8c;
  }
  html, body {
    margin: 0;
    padding: 0;
    width: 1200px;
    height: 1000px;
    overflow: hidden;
    background: var(--backdrop);
    font-family: "Open Sans", Arial, sans-serif;
  }
  .canvas {
    position: relative;
    width: 1200px;
    height: 1000px;
  }
  .card {
    position: absolute;
    background: var(--card-paper);
    box-shadow: 0 2px 8px rgba(0,0,0,0.35);
  }
  .card--front {
    left: 52px;
    top: 40px;
    width: 684px;
    height: 440px;
  }
  .card--back {
    left: 452px;
    top: 520px;
    width: 686px;
    height: 440px;
  }
  .wordmark {
    position: absolute;
    left: 0;
    right: 0;
    text-align: center;
    color: var(--brand-green);
    font-weight: 700;
    letter-spacing: -3px;
    line-height: 1;
  }
  .card--front .wordmark {
    top: 162px;
    font-size: 92px;
  }
  .card--back .wordmark {
    top: 68px;
    font-size: 70px;
    letter-spacing: -2px;
  }
  .holder-name {
    position: absolute;
    left: 0;
    right: 0;
    top: 216px;
    text-align: center;
    color: var(--brand-green);
    font-size: 26px;
    font-weight: 700;
    letter-spacing: 0.5px;
  }
  .contact {
    position: absolute;
    display: flex;
    align-items: center;
    gap: 8px;
    color: var(--brand-grey);
    font-size: 18px;
    letter-spacing: 0.3px;
    white-space: nowrap;
  }
  .contact svg {
    width: 20px;
    height: 20px;
    flex: none;
  }
  .contact--address { left: 22px; top: 314px; }
  .contact--phone   { left: 22px; top: 356px; }
  .contact--mobile  { left: 22px; top: 397px; }
  .contact--email   { left: 338px; top: 354px; }
  .contact--web     { left: 338px; top: 397px; }
</style>
</head>
<body>
<div class="canvas">

  <section class="card card--front">
    <div class="wordmark">BluePlinth</div>
  </section>

  <section class="card card--back">
    <div class="wordmark">BluePlinth</div>
    <div class="holder-name">JENNA CALDWELL</div>

    <div class="contact contact--address">
      <svg viewBox="0 0 20 20" aria-hidden="true">
        <rect width="20" height="20" rx="6" fill="var(--brand-green)"/>
        <path d="M10 4 L16 9.5 H14 V15 H11.5 V11.5 H8.5 V15 H6 V9.5 H4 Z" fill="#fff"/>
      </svg>
      <span>22a Fenwick Road, Ely, Cambridgeshire, CB7 4RT</span>
    </div>

    <div class="contact contact--phone">
      <svg viewBox="0 0 20 20" aria-hidden="true">
        <rect width="20" height="20" rx="6" fill="var(--brand-green)"/>
        <path d="M6 4.5 L8.3 4.5 L9 7.5 L7.6 8.6 C8.4 10.3 9.7 11.6 11.4 12.4 L12.5 11 L15.5 11.7 L15.5 14 C15.5 14.8 14.8 15.5 14 15.5 C8.8 15.2 4.8 11.2 4.5 6 C4.5 5.2 5.2 4.5 6 4.5 Z" fill="#fff"/>
      </svg>
      <span>01353 482917</span>
    </div>

    <div class="contact contact--mobile">
      <svg viewBox="0 0 20 20" aria-hidden="true">
        <rect width="20" height="20" rx="6" fill="var(--brand-green)"/>
        <rect x="6.5" y="3.5" width="7" height="13" rx="1.2" fill="#fff"/>
        <rect x="7.8" y="5" width="4.4" height="7" fill="var(--brand-green)"/>
        <circle cx="10" cy="14.3" r="0.9" fill="var(--brand-green)"/>
      </svg>
      <span>07812559034</span>
    </div>

    <div class="contact contact--email">
      <svg viewBox="0 0 20 20" aria-hidden="true">
        <rect width="20" height="20" rx="6" fill="var(--brand-green)"/>
        <rect x="4" y="6" width="12" height="8.5" fill="#fff"/>
        <path d="M4 6 L10 11 L16 6" fill="none" stroke="var(--brand-green)" stroke-width="1.2"/>
      </svg>
      <span>jenna.caldwell@plinthdata.com</span>
    </div>

    <div class="contact contact--web">
      <svg viewBox="0 0 20 20" aria-hidden="true">
        <rect width="20" height="20" rx="6" fill="var(--brand-green)"/>
        <circle cx="6.5" cy="13.5" r="1.6" fill="#fff"/>
        <path d="M5 9 A6 6 0 0 1 11 15" fill="none" stroke="#fff" stroke-width="1.8"/>
        <path d="M5 5 A10 10 0 0 1 15 15" fill="none" stroke="#fff" stroke-width="1.8"/>
      </svg>
      <span>www.blueplinth.com</span>
    </div>
  </section>

</div>
</body>
</html>
```